CRPG is needing business cards, and stationary created.

Pixel Forge created a logo for our business, and now we are wanting business cards, and stationary. I have included two designs of the same logo. Please feel free to use them as you want. The name of the company is Cedar Ridge Property Group LLC, the address is 812 NE Willow Ln., Suite 9, the city & state is Harlow Springs, Nevada, zip code is 97815, Telephone number is 541-327-4489, Fax number is 541-327-6051, the name on the business card is Carl Whitby CMCA

Industry/Entity Type

Property Management

Contact Information for Business Card

The card needs to look professional. Upscale.

Requirements
Must have
• The colors we are using are on the logo that has been uploaded.

```html
<!DOCTYPE html>
<html lang="en">
<head>
<meta charset="utf-8">
<title>Cedar Ridge Property Group – Business Card</title>
<link href="https://fonts.googleapis.com/css2?family=Work+Sans:wght@400;500;700&display=swap" rel="stylesheet">
<style>
  :root {
    --navy: #3a4a5e;
    --teal: #14876f;
    --paper: #ffffff;
    --backdrop: #2b2b2b;
    --text-light: #e9edf2;
  }
  * { margin: 0; padding: 0; box-sizing: border-box; }
  html, body { width: 1200px; height: 900px; overflow: hidden; }
  body {
    background: var(--backdrop);
    font-family: "Work Sans", Arial, sans-serif;
    display: flex;
    flex-direction: column;
    align-items: center;
    justify-content: center;
    gap: 40px;
  }
  .card {
    position: relative;
    width: 700px;
    height: 400px;
    overflow: hidden;
    box-shadow: 0 12px 30px rgba(0,0,0,.45);
  }
  .card-front { background: var(--paper); }
  .front-band { position: absolute; inset: 0; width: 100%; height: 100%; }
  .brand { display: flex; align-items: center; gap: 14px; }
  .brand-mark { width: 34px; height: 34px; flex: none; }
  .brand-name { font-weight: 700; letter-spacing: 1px; text-transform: uppercase; white-space: nowrap; }
  .card-front .brand { position: absolute; left: 48px; top: 40px; }
  .card-front .brand-mark { background: var(--teal); }
  .card-front .brand-name { color: var(--teal); font-size: 30px; }
  .holder { position: absolute; left: 48px; top: 104px; }
  .holder-name { font-size: 26px; font-weight: 500; color: var(--navy); letter-spacing: .5px; text-transform: uppercase; }
  .holder-title { font-size: 16px; font-weight: 500; color: var(--teal); margin-top: 2px; }
  .contact {
    position: absolute;
    left: 48px;
    top: 214px;
    list-style: none;
    color: var(--text-light);
    font-size: 15px;
    line-height: 24px;
  }
  .contact li { display: flex; align-items: center; gap: 10px; white-space: nowrap; }
  .contact svg { width: 12px; height: 12px; fill: var(--text-light); flex: none; }
  .contact .address { padding-left: 22px; }
  .card-back { background: var(--navy); display: flex; align-items: center; justify-content: center; }
  .card-back .brand-mark { background: var(--paper); width: 44px; height: 44px; }
  .card-back .brand-name { color: var(--paper); font-size: 40px; }
</style>
</head>
<body>

<section class="card card-front" aria-label="Business card front">
  <svg class="front-band" viewBox="0 0 700 400" preserveAspectRatio="none" aria-hidden="true">
    <polygon points="0,180 0,400 700,400 700,360 420,180" fill="var(--navy)"/>
  </svg>

  <div class="brand">
    <span class="brand-mark"></span>
    <span class="brand-name">Cedar Ridge</span>
  </div>

  <div class="holder">
    <p class="holder-name">Carl Whitby</p>
    <p class="holder-title">CMCA</p>
  </div>

  <ul class="contact">
    <li><svg viewBox="0 0 12 12"><path d="M2.5 0.5l2 2.2-1 1.3a7 7 0 0 0 4.5 4.5l1.3-1 2.2 2-1.5 2A10 10 0 0 1 0.5 2z"/></svg>555-327-4489</li>
    <li><svg viewBox="0 0 12 12"><path d="M3 0h6v3H3zM0 4h12v6h-2v2H2v-2H0zM3 8v3h6V8z"/></svg>555-327-6051</li>
    <li><svg viewBox="0 0 12 12"><path d="M0 2h12v8H0zM1 3v.4l5 3.2 5-3.2V3zM1 4.6V9h10V4.6L6 7.8z"/></svg>info@crpgllc.com</li>
    <li><svg viewBox="0 0 12 12"><circle cx="6" cy="6" r="6"/></svg>www.crpgllc.com</li>
    <li class="address">812 NE Willow Ln., Suite 9,</li>
    <li class="address">Harlow Springs, Nevada, 97815</li>
  </ul>
</section>

<section class="card card-back" aria-label="Business card back">
  <div class="brand">
    <span class="brand-mark"></span>
    <span class="brand-name">Cedar Ridge</span>
  </div>
</section>

</body>
</html>
```